High end cable company busines card and letterhead

Dear designers,
We assemble high end audio cables that cost a couple of hundred dollars per piece and we are improving the looks of the product.
When people buy a cable they get a leather pouch with the invoice (letterhead) , a business card of the maker and also a quality control card  / warranty card.
The quality control card  is the same size as a business card and the back of the quality control card is the same back as the business card. So we need 4 things:
-1 back of a business card
-1 front of a business card (a file where we can change the name and details of the worker)
-1 quality control front (I will add a photo of an example)
-1 letterhead
We want to make letterpress business cards and use shiny foil for the logo’s. We like the colors black and copper or black and gold for the back. The front of the business card can also be black, copper and white but it does not have to be those colors. We want people to have the feeling that they bought something expensive and high quality.
The front of the quality control card has to be white so we can check things off with a sharpie / pen.
What has to be on the cards:
Business card:
- Our Logo
-Text: Meet the maker (people get the business card of the one who made the cable)
-Name
-Address
-Website (www.talvickwire.com)
-Email address
-Text: For any advise or questions about your cable feel free to contact me.
What has to be on the quality control card:
-Our logo
-Text: quality controll and warranty card (small at the bottom)
-text:
Assembled by:________________
Date: ______-______-____________
QC by:_________________________

Assembly QC [   ]
Measurement QC [   ]
Aesthetics [   ]
(The box [    ] is for the initials of the person that does the QC, it can also be a line or something else)
The letterhead can be your own idea as long as it looks luxurious.
You can download our logo. We have a black one and gold / black but you can change the Color to Match your design. (For instance copper or something) There is also a white one that can be used with the icon on the left.
Some links of stuff we like:
-https://clipvault.example/Rk4wQz81mTa (The looks of this card maybe a bit less busy looking)
-https://b.shopmarrow.com/_qTrvWak
-https://b.shopmarrow.com/_qBu3Lod
-https://b.shopmarrow.com/_qEyaz77

```html
<!DOCTYPE html>
<html lang="en">
<head>
<meta charset="utf-8">
<title>Talvick &amp; Wire — Business Card</title>
<link rel="stylesheet" href="https://fonts.googleapis.com/css2?family=Poppins:ital,wght@0,400;0,500;0,600;1,400&family=Montserrat:wght@500;700&display=swap">
<style>
  :root {
    --backdrop: #1c1c1e;
    --card: #141415;
    --card-edge: #1f1f21;
    --ink: #f4f4f4;
    --gold: #e9a623;
    --icon-yellow: #f2d214;
    --emboss: #1b1b1d;
    --divider: #bdbdbd;
  }
  * { margin: 0; padding: 0; box-sizing: border-box; }
  html, body {
    width: 1200px; height: 1200px; overflow: hidden;
    background: var(--backdrop);
    font-family: "Poppins", sans-serif;
    color: var(--ink);
  }
  .canvas { position: relative; width: 1200px; height: 1200px; }

  .card {
    position: absolute; left: 150px; width: 900px; height: 514px;
    background: var(--card);
    border-radius: 22px;
    box-shadow: 0 18px 40px rgba(0,0,0,.55), inset 0 0 0 1px var(--card-edge);
    overflow: hidden;
  }
  .card--back { top: 66px; }
  .card--front { top: 620px; }

  /* back of card */
  .pattern-field {
    position: absolute; top: 120px; width: 250px; height: 180px;
    background: linear-gradient(135deg, var(--emboss), #121213 60%, var(--emboss));
    border-radius: 4px; opacity: .9;
  }
  .pattern-field--left { left: 40px; }
  .pattern-field--right { right: 40px; top: 200px; }
  .brand--back {
    position: absolute; left: 0; right: 0; top: 150px;
    display: flex; flex-direction: column; align-items: center; gap: 28px;
  }
  .brand-mark--back {
    width: 110px; height: 110px; background: var(--gold);
  }
  .brand-name--foil {
    font-weight: 500; font-size: 40px; line-height: 1; color: var(--gold);
  }

  /* front of card */
  .brand--front {
    position: absolute; left: 80px; top: 56px;
    display: flex; align-items: center; gap: 26px;
  }
  .brand-mark--front { width: 96px; height: 96px; background: var(--ink); }
  .brand-name {
    font-weight: 500; font-size: 40px; line-height: 1; color: var(--ink);
  }
  .tagline {
    position: absolute; left: 90px; top: 232px;
    font-weight: 500; font-size: 22px; letter-spacing: 1px;
  }
  .divider {
    position: absolute; left: 372px; top: 210px; width: 1px; height: 190px;
    background: var(--divider);
  }
  .maker { position: absolute; left: 410px; top: 208px; }
  .maker__name {
    font-family: "Montserrat", sans-serif; font-weight: 700;
    font-size: 26px; letter-spacing: 3px;
  }
  .maker__address {
    margin-top: 14px; font-family: "Montserrat", sans-serif; font-weight: 500;
    font-size: 19px; letter-spacing: 1.5px; line-height: 1.45; font-style: normal;
  }
  .contact-list { list-style: none; margin-top: 16px; }
  .contact-list li {
    display: flex; align-items: center; gap: 14px;
    font-family: "Montserrat", sans-serif; font-weight: 500;
    font-size: 19px; letter-spacing: 1.5px; line-height: 1.5;
  }
  .contact-list svg { width: 20px; height: 20px; flex: none; }
  .invitation {
    position: absolute; left: 90px; right: 40px; top: 448px;
    font-style: italic; font-size: 20px;
  }
</style>
</head>
<body>
<main class="canvas">

  <section class="card card--back" aria-label="Business card back">
    <div class="pattern-field pattern-field--left" role="img" aria-label="Blind-embossed geometric pattern"></div>
    <div class="pattern-field pattern-field--right" role="img" aria-label="Blind-embossed geometric pattern"></div>
    <div class="brand brand--back">
      <span class="brand-mark--back" aria-hidden="true"></span>
      <p class="brand-name--foil">Talvick &amp; Wire</p>
    </div>
  </section>

  <section class="card card--front" aria-label="Business card front">
    <div class="brand brand--front">
      <span class="brand-mark--front" aria-hidden="true"></span>
      <p class="brand-name">Talvick &amp; Wire</p>
    </div>

    <p class="tagline">MEET THE MAKER</p>
    <div class="divider"></div>

    <div class="maker">
      <p class="maker__name">EVAN HOLLIS</p>
      <address class="maker__address">
        118 Larkspur Street<br>
        Suite 210, Brookhaven<br>
        OR 97411
      </address>
      <ul class="contact-list">
        <li>
          <svg viewBox="0 0 24 24" aria-hidden="true"><path fill="var(--icon-yellow)" d="M6.6 10.8a15.1 15.1 0 0 0 6.6 6.6l2.2-2.2a1 1 0 0 1 1-.25 11.4 11.4 0 0 0 3.6.57 1 1 0 0 1 1 1V20a1 1 0 0 1-1 1A17 17 0 0 1 3 4a1 1 0 0 1 1-1h3.5a1 1 0 0 1 1 1c0 1.25.2 2.45.57 3.57a1 1 0 0 1-.25 1z"/></svg>
          www.talvickwire.com
        </li>
        <li>
          <svg viewBox="0 0 24 24" aria-hidden="true"><rect x="2" y="5" width="20" height="14" rx="1.5" fill="var(--icon-yellow)"/><path d="M2.5 6l9.5 7 9.5-7" fill="none" stroke="var(--card)" stroke-width="1.5"/></svg>
          evan@talvickmail.example
        </li>
      </ul>
    </div>

    <p class="invitation">For any advise or questions about your cable feel free to contact me.</p>
  </section>

</main>
</body>
</html>
```